Gorvane Rum Liqueur Bottle Label

I will be launching a Rum Liqueur called Gorvane Spiced Rum Liqueur. The bottle I have chosen to use is an TKV 500ml type and I have included a photo of it in the project brief. The bottle dimensions are height 193.5mm with diameter 85mm. There will be a cork closure, sealed with a heat shrink capsule. I require two labels for each bottle, a large rectangular label on the front with the product name, logo, label design and the bottle quantity which is 500ml. The front label should also contain the strength of the liqueur which is 25% vol. The rear label will contain the required UK legal information such as government health warning, number of UK units of alcohol as well as the place of bottling which is Wick, Caithness, Scotland. A barcode will also be on the rear label and I have added it as a jpg file. On my current homemade label I also have the following text on the rear label: "Due to the ferocious tides, currents and winds that shape the narrow stretch of water separating Caithness from the Orkney Islands in the far North of Scotland, it has become known to generations of sailors as "Gorvane" and is the graveyard of countless number of ships. Gorvane Spiced Rum Liqueur aims to capture the spirit of those brave men and women who have risked all on these treacherous shores". For the main front label I am keen for the designer to explore the themes of shipwreck, sea monsters, smuggling, pistols, diving helmets, heavy seas, sea stacks, high cliffs, sealife etc. I have included a story about a local smuggler called Peter Lurrick as an example of an inspirational theme. I currently also have a website regarding Caithness shipwrecks which can be found at www.gorvane-example.com and which could provide some further ideas. My feeling is that the label design should be masculine and I would like to keep away from designs that would make the label costly to print. I have included a file with my current logo but please feel free to change its colour as required and to remove the word Gorvane from the logo if you wish. I can supply the logo file in different formats such as jpg, ai, eps, pdf, png or psd. I also have the barcode in pdf, png or svg formats. The word Gorvane is a registered trademark.I have also attached a photograph of my liqueur in an attempt to show the colour of the finished product and the bottle style.
Colors
Designer to choose colors to be used in the design.
Look and feel
Each slider illustrates characteristics of the customer's brand and the style your logo design should communicate.

```html
<!DOCTYPE html>
<html lang="en">
<head>
<meta charset="utf-8">
<title>Gorvane Spiced Rum Liqueur – Front Label</title>
<link rel="stylesheet" href="https://fonts.googleapis.com/css2?family=UnifrakturCook:wght@700&family=Permanent+Marker&display=swap">
<style>
  :root {
    --backdrop: #0b5960;
    --label-teal: #0f6c74;
    --deep-teal: #06343a;
    --mid-teal: #0d4c53;
    --sea-teal: #2a7f86;
    --gold: #d59b2b;
    --spec-ink: #052a2e;
  }
  * { margin: 0; padding: 0; box-sizing: border-box; }
  html, body {
    width: 1200px;
    height: 866px;
    overflow: hidden;
    background: var(--backdrop);
  }
  .canvas {
    position: relative;
    width: 1200px;
    height: 866px;
  }
  .front-label {
    position: absolute;
    left: 340px;
    top: 123px;
    width: 520px;
    height: 620px;
    background: var(--label-teal);
    overflow: hidden;
  }
  .brand-mark {
    position: absolute;
    top: 40px;
    left: 0;
    width: 100%;
    display: flex;
    justify-content: center;
    align-items: center;
    gap: 12px;
  }
  .brand-mark__dot {
    width: 14px;
    height: 14px;
    border-radius: 50%;
    background: var(--gold);
  }
  .brand-mark__name {
    font-family: "Permanent Marker", "Comic Sans MS", cursive;
    font-size: 32px;
    line-height: 1;
    color: var(--gold);
    letter-spacing: 2px;
  }
  .shipwreck-scene {
    position: absolute;
    left: 20px;
    top: 120px;
    width: 480px;
    height: 330px;
  }
  .product-name {
    position: absolute;
    top: 372px;
    left: 0;
    width: 100%;
    text-align: center;
    padding-left: 40px;
    font-family: "UnifrakturCook", serif;
    font-weight: 700;
    font-size: 72px;
    line-height: 1;
    color: var(--gold);
    text-shadow: 4px 6px 8px rgba(0,0,0,0.55);
  }
  .product-type {
    position: absolute;
    top: 470px;
    left: 0;
    width: 100%;
    text-align: center;
    font-family: "Permanent Marker", "Comic Sans MS", cursive;
    font-size: 34px;
    line-height: 1;
    color: var(--gold);
    letter-spacing: 2px;
    white-space: nowrap;
  }
  .label-specs {
    position: absolute;
    top: 560px;
    left: 96px;
    right: 84px;
    display: flex;
    justify-content: space-between;
    font-family: "Permanent Marker", "Comic Sans MS", cursive;
    font-size: 17px;
    line-height: 1;
    color: var(--spec-ink);
  }
</style>
</head>
<body>
<main class="canvas">
  <section class="front-label">
    <div class="brand-mark">
      <span class="brand-mark__dot"></span>
      <span class="brand-mark__name">Gorvane</span>
    </div>
    <svg class="shipwreck-scene" viewBox="0 0 480 330" role="img" aria-label="Illustration of a tall sailing ship wrecked in heavy seas">
      <defs>
        <radialGradient id="scene-shade" cx="50%" cy="48%" r="55%">
          <stop offset="0%" stop-color="var(--deep-teal)"/>
          <stop offset="55%" stop-color="var(--mid-teal)"/>
          <stop offset="85%" stop-color="var(--sea-teal)" stop-opacity="0.6"/>
          <stop offset="100%" stop-color="var(--label-teal)" stop-opacity="0"/>
        </radialGradient>
      </defs>
      <path d="M40 150 C60 60 170 20 250 30 C350 40 440 90 450 170 C460 250 400 310 300 318 L90 318 C40 300 20 220 40 150 Z" fill="url(#scene-shade)"/>
    </svg>
    <h1 class="product-name">gorvane</h1>
    <p class="product-type">SPICED RUM LIQUEUR</p>
    <div class="label-specs">
      <span class="label-specs__volume">500ml</span>
      <span class="label-specs__strength">25% Vol.</span>
    </div>
  </section>
</main>
</body>
</html>
```